landscape and garden design business card

I would like a business card designed for my landscape and garden design company, Wrenfield Landscapes. We are located in Colorado. I would like to include our logo, contact info, and social media/web site address or QR code. Looking for an organic, flowing design that incorporates our logo.

Target Market(s)

Homeowners and businesses that need garden and landscape design

Contact Information for Business Card

Would like it to say landscape and garden design

Requirements
Must have
• Landscape and garden design

```html
<!DOCTYPE html>
<html lang="en">
<head>
<meta charset="utf-8">
<title>Wrenfield Landscapes – Business Card</title>
<link href="https://fonts.googleapis.com/css2?family=Poppins:wght@400;600&display=swap" rel="stylesheet">
<style>
  :root {
    --page-bg: #1b1e1f;
    --card-bg: #243433;
    --ink: #bdbcae;
    --ink-soft: #a9a99c;
  }
  * { box-sizing: border-box; margin: 0; padding: 0; }
  html, body {
    width: 1200px; height: 900px; overflow: hidden;
    background: var(--page-bg);
    font-family: "Poppins", sans-serif;
    color: var(--ink);
  }
  .canvas {
    position: relative; width: 1200px; height: 900px;
    display: flex; flex-direction: column; align-items: center;
    justify-content: center; gap: 24px;
  }
  .card {
    position: relative; width: 700px; height: 400px;
    background: var(--card-bg);
    box-shadow: 0 10px 30px rgba(0,0,0,.45);
  }
  /* Brand mark: plain circle + name */
  .brand { display: flex; flex-direction: column; align-items: center; }
  .brand-disc {
    border-radius: 50%; background: var(--ink);
  }
  .brand-name {
    font-weight: 400; color: var(--ink); text-align: center; line-height: 1.15;
  }
  /* Back face */
  .card-back {
    display: flex; flex-direction: column; align-items: center; justify-content: center;
  }
  .card-back .brand-disc { width: 150px; height: 150px; margin-bottom: 18px; }
  .card-back .brand-name { font-size: 38px; }
  .card-back .tagline { font-size: 14px; letter-spacing: 2px; margin-top: 6px; color: var(--ink-soft); text-transform: uppercase; }
  .social-handle { margin-top: 26px; font-size: 16px; color: var(--ink); }
  /* Front face */
  .card-front { display: flex; align-items: center; padding: 0 50px 0 40px; }
  .card-front .brand { width: 270px; }
  .card-front .brand-disc { width: 170px; height: 170px; margin-bottom: 16px; }
  .card-front .brand-name { font-size: 34px; }
  .card-front .tagline { font-size: 11px; letter-spacing: 1.5px; margin-top: 6px; color: var(--ink-soft); text-transform: uppercase; }
  .divider { width: 2px; height: 250px; background: var(--ink); margin: 0 30px 0 36px; }
  .contact { flex: 1; }
  .person-name { font-size: 22px; font-weight: 600; letter-spacing: 1.5px; text-transform: uppercase; }
  .person-role { font-size: 17px; margin-bottom: 16px; }
  .address { font-size: 16px; line-height: 1.45; margin-bottom: 16px; }
  .contact-list { list-style: none; font-size: 16px; line-height: 1.6; }
  .contact-list li { display: flex; align-items: center; gap: 10px; }
  .contact-list svg { width: 15px; height: 15px; flex: none; fill: var(--ink); }
</style>
</head>
<body>
<main class="canvas">
  <section class="card card-back" aria-label="Card back">
    <div class="brand">
      <div class="brand-disc"></div>
      <p class="brand-name">Wrenfield Landscapes</p>
      <p class="tagline">Landscape and garden design</p>
    </div>
    <p class="social-handle">@wrenfieldlandscapes</p>
  </section>

  <section class="card card-front" aria-label="Card front">
    <div class="brand">
      <div class="brand-disc"></div>
      <p class="brand-name">Wrenfield Landscapes</p>
      <p class="tagline">Landscape and garden design</p>
    </div>
    <div class="divider"></div>
    <div class="contact">
      <p class="person-name">Daniel Mercer</p>
      <p class="person-role">Development Manager Officer</p>
      <p class="address">412 Aspen Ridge Road<br>Suite 210, Boulder, CO 80302</p>
      <ul class="contact-list">
        <li>
          <svg viewBox="0 0 24 24" aria-hidden="true"><path d="M6.6 10.8a15.1 15.1 0 0 0 6.6 6.6l2.2-2.2c.3-.3.7-.4 1-.2 1.1.4 2.3.6 3.6.6.6 0 1 .4 1 1V20c0 .6-.4 1-1 1A17 17 0 0 1 3 4c0-.6.4-1 1-1h3.5c.6 0 1 .4 1 1 0 1.3.2 2.5.6 3.6.1.3 0 .7-.2 1z"/></svg>
          303-555-0147
        </li>
        <li>
          <svg viewBox="0 0 24 24" aria-hidden="true"><path d="M2 5h20v14H2z M2 5l10 8 10-8" /></svg>
          daniel@wrenfieldgardens.com
        </li>
        <li>
          <svg viewBox="0 0 24 24" aria-hidden="true"><path d="M12 2a10 10 0 1 0 0 20 10 10 0 0 0 0-20zm0 2c.9 0 2.2 2 2.7 5H9.3C9.8 6 11.1 4 12 4zM4.3 11h3.8a17 17 0 0 0 0 2H4.3a8 8 0 0 1 0-2zm5 0h5.4a15 15 0 0 1 0 2H9.3a15 15 0 0 1 0-2zm6.6 0h3.8a8 8 0 0 1 0 2h-3.8a17 17 0 0 0 0-2zM9.3 15h5.4c-.5 3-1.8 5-2.7 5s-2.2-2-2.7-5z"/></svg>
          wrenfieldgardens.com
        </li>
      </ul>
    </div>
  </section>
</main>
</body>
</html>
```